Roofing Contractor website

I currently have a website. But I would like it redesigned. Here is my website:
www.brambletopshingle.co

I want to try and mimic the look of another website: www.vestapixelworks.com

For legal reasons I don’t want to copy it 100%, but I would like to copy it as much as possible because I like the look and simplicity of this website. We have similar colors. My company colors are black, red and white.

I am not very good at web design, but I am good enough to go into front page and change some text and images if the main design is already created for me. I am looking for someone to basically create 95% of this front page site for me, and I can go in and tweak some of the wording and images later.

My current website already has SEO work done. So I do not want to lose the work that is done already because I am currently ranked very well in my area. I just want the design of my site to change but not lose any seo rankings.

I attached some wording id like to replace from the vesta pixelworks website. But this is NOT complete. Just some notes I wrote down. We can get together to make this more complete later.

The most important things to me is that I do not lose SEO and the overall look and design is similar to vesta pixelworks website but its designed for my brambletop shingle website.

Coding

```html
<!DOCTYPE html>
<html lang="en">
<head>
<meta charset="utf-8">
<title>Brambletop Shingle – Residential and Commercial Roofing Company</title>
<link href="https://fonts.googleapis.com/css2?family=Archivo:wght@500;700;800;900&family=Jost:wght@400;500&display=swap" rel="stylesheet">
<style>
  :root{
    --black:#000;
    --ink:#161616;
    --charcoal:#2a2a2a;
    --white:#fff;
    --red:#e10b0b;
    --red-deep:#b30404;
    --red-band:#9c0000;
    --red-shadow:#5e0000;
    --cream:#f4f1c9;
    --grey-logo:#9a9a9a;
  }
  *{box-sizing:border-box;margin:0;padding:0}
  html,body{width:1200px;height:2958px;overflow:hidden;background:var(--black)}
  body{position:relative;font-family:'Jost',sans-serif;color:var(--white)}
  .abs{position:absolute}
  .display{font-family:'Archivo',sans-serif;font-weight:900;text-transform:uppercase;letter-spacing:.2px}

  /* Header */
  .site-header{left:0;top:0;width:1200px;height:98px;background:var(--black);z-index:3}
  .brand{left:104px;top:30px;width:140px;text-align:center}
  .brand-mark{width:44px;height:44px;border-radius:50%;background:var(--red);margin:0 auto 6px}
  .brand-name{font-family:'Archivo',sans-serif;font-weight:800;font-size:14px;color:var(--white);line-height:1.1;text-transform:uppercase}
  .nav a{position:absolute;top:38px;font-size:16px;color:var(--white);text-decoration:none}
  .btn{display:flex;align-items:center;border-radius:10px;overflow:hidden;background:var(--red-deep);color:var(--white);font-family:'Archivo',sans-serif;font-weight:700}
  .btn .arrow{background:var(--red);height:100%;display:flex;align-items:center;justify-content:center}
  .btn-intro{left:864px;top:23px;width:240px;height:50px;font-size:19px}
  .btn-intro .label{padding-left:12px;flex:1}
  .btn-intro .arrow{width:58px}

  /* Hero */
  .hero{left:0;top:98px;width:1200px;height:637px;background:var(--black);overflow:hidden}
  .hero-photo{left:380px;top:0;width:820px;height:637px;
    background:linear-gradient(180deg,#2f4f7a 0%,#5a6a78 22%,#8a6a44 45%,#3d4a5c 62%,#123a8a 80%,#0a1f5a 100%)}
  .hero-fade{left:380px;top:0;width:820px;height:637px;
    background:linear-gradient(90deg,#000 0%,rgba(0,0,0,.85) 18%,rgba(0,0,0,0) 55%),
               linear-gradient(0deg,rgba(0,0,0,.4) 0%,rgba(0,0,0,0) 25%)}
  .hero-title{left:101px;top:150px;font-size:47px;line-height:54px}
  .hero-title .accent{color:var(--red)}
  .hero-sub{left:101px;top:340px;font-size:16.5px;line-height:27px}
  .btn-call{left:101px;top:438px;width:240px;height:51px;font-size:19px}
  .btn-call .label{display:flex;align-items:center;gap:12px;padding-left:14px;flex:1}
  .btn-call .arrow{width:57px}
  .trust{left:101px;top:536px;height:34px;display:flex;align-items:center;font-family:'Archivo',sans-serif;font-size:10px;font-weight:500}
  .trust .g{font-family:'Archivo',sans-serif;font-weight:900;font-size:32px;margin-right:20px}
  .trust .sep{width:1px;height:32px;background:var(--white);margin:0 22px}
  .trust .badge{width:66px;height:30px;background:#1c2b9c;border-radius:4px;position:relative}
  .trust .badge::before{content:"";position:absolute;left:0;top:0;width:24px;height:30px;background:var(--red);border-radius:4px 0 0 4px}

  /* Services */
  .services{left:0;top:735px;width:1200px;height:760px;background:var(--black)}
  .services-photo{left:44px;top:70px;width:443px;height:602px;border:9px solid var(--cream);border-radius:10px;
    background:linear-gradient(160deg,#6a7a5a 0%,#d7d4cc 25%,#c8c2b6 50%,#8a7c6c 75%,#4a4440 100%)}
  .section-title{font-size:38px;line-height:44px}
  .section-title .accent{color:var(--red)}
  .services .section-title{left:514px;top:128px}
  .services-lead{left:520px;top:183px;font-size:23px}
  .tabs{left:512px;top:278px;width:564px;height:52px;border-bottom:2px solid var(--white)}
  .tab{position:absolute;top:0;font-family:'Archivo',sans-serif;font-weight:800;font-size:26px}
  .tab-active::after{content:"";position:absolute;left:-13px;top:48px;width:233px;height:4px;background:var(--red)}
  .services-copy{left:521px;top:378px;width:550px;font-size:15px;line-height:25px}
  .service-item{display:flex;align-items:center;font-family:'Archivo',sans-serif;font-weight:800;font-size:21px}
  .service-item svg{margin-right:24px}

  /* Endorse */
  .endorse{left:0;top:1495px;width:1200px;height:741px;background:var(--charcoal)}
  .endorse-photo{left:590px;top:74px;width:610px;height:484px;border-radius:14px 0 0 14px;
    background:linear-gradient(135deg,#2f6ed8 0%,#8d98a6 28%,#d8dcdf 45%,#6b6f74 62%,#a35a22 80%,#3a2a1e 100%)}
  .endorse-card{left:0;top:140px;width:786px;height:523px;background:var(--ink);border-radius:0 12px 12px 0}
  .endorse .section-title{left:42px;top:122px;font-size:38px;line-height:44px}
  .endorse-points{left:55px;top:268px;font-size:26px;line-height:75px}

  /* Partners */
  .partners{left:0;top:2236px;width:1200px;height:336px;background:var(--black)}
  .partner{position:absolute;top:164px;width:140px;display:flex;align-items:center;gap:6px;color:var(--grey-logo);font-family:'Archivo',sans-serif;font-weight:800;font-size:21px}
  .partner .dot{width:18px;height:18px;border-radius:50%;background:var(--grey-logo);flex:none}
  .partner small{display:block;font-size:9px;font-weight:700;line-height:10px}

  /* Process */
  .process{left:0;top:2572px;width:1200px;height:386px;background:var(--red-band);border-top:2px solid #5a0000}
  .process-title{left:50px;top:118px;font-size:38px;line-height:40px}
  .process-title .shade{color:var(--red-shadow)}
  .process-tagline{left:792px;top:118px;font-size:35px;line-height:57px}
  .step{position:absolute;top:336px;width:344px;height:60px;border-radius:14px 14px 0 0;overflow:hidden;
    background:linear-gradient(90deg,#d2d2d2 0%,#8a8a8a 40%,#5a5a5a 70%,#cfcfcf 100%)}
  .step .num{position:absolute;left:12px;top:6px;font-family:'Archivo',sans-serif;font-weight:900;font-size:40px;color:var(--white)}
</style>
</head>
<body>

<header class="abs site-header">
  <div class="abs brand">
    <div class="brand-mark"></div>
    <div class="brand-name">Brambletop Shingle</div>
  </div>
  <nav class="nav">
    <a style="left:366px">About</a>
    <a style="left:433px">Services</a>
    <a style="left:520px">Projects</a>
    <a style="left:605px">Budget</a>
    <a style="left:684px">Indicator</a>
    <a style="left:781px">More</a>
  </nav>
  <a class="abs btn btn-intro"><span class="label">Schedule Intro Call</span>
    <span class="arrow"><svg width="24" height="14" viewBox="0 0 24 14"><path d="M1 7h21M16 1l6 6-6 6" fill="none" stroke="#fff" stroke-width="2"/></svg></span></a>
</header>

<section class="abs hero">
  <div class="abs hero-photo" role="img" aria-label="Modern home with lit interior and swimming pool at dusk"></div>
  <div class="abs hero-fade"></div>
  <h1 class="abs display hero-title">Residential and<br>Commercial<br><span class="accent">Roofing Company</span></h1>
  <p class="abs hero-sub">Best roofing controller in Millbrook, TX<br>LifeTime Warranty Catch all Net</p>
  <a class="abs btn btn-call"><span class="label">
      <svg width="24" height="24" viewBox="0 0 24 24"><path d="M6 3l3 4-2 2c1 3 4 6 7 7l2-2 4 3-2 3C11 20 4 13 3 5z" fill="none" stroke="#fff" stroke-width="1.6"/></svg>
      Give Us a Call</span>
    <span class="arrow"><svg width="24" height="14" viewBox="0 0 24 14"><path d="M1 7h21M16 1l6 6-6 6" fill="none" stroke="#fff" stroke-width="2"/></svg></span></a>
  <div class="abs trust">
    <span class="g">F</span><span>5 star Findwell<br>Reveiw</span>
    <span class="sep"></span>
    <span class="badge" role="img" aria-label="Lifetime warranty badge"></span>
    <span class="sep"></span>
    <span>Catch all Net</span>
  </div>
</section>

<section class="abs services">
  <svg class="abs" style="left:200px;top:330px" width="320" height="110" viewBox="0 0 320 110">
    <path d="M290 2c14 8 22 20 22 40v40c0 14-8 22-22 22H6" fill="none" stroke="#e10b0b" stroke-width="8"/>
    <path d="M160 104h40M210 104h30M250 104h30" stroke="#3a0000" stroke-width="8" stroke-dasharray="14 8"/>
  </svg>
  <svg class="abs" style="left:480px;top:330px;display:none" width="1" height="1"></svg>
  <div class="abs services-photo" role="img" aria-label="Bright showroom interior with pendant lamps and a kitchen island"></div>
  <h2 class="abs display section-title">Our Home <span class="accent">Services</span></h2>
  <p class="abs services-lead">We love serving a community</p>
  <div class="abs tabs">
    <span class="tab tab-active" style="left:13px">Residential</span>
    <span class="tab" style="left:302px">Commercial</span>
  </div>
  <p class="abs services-copy">Lorem ipsum dolor sit amet, consectetur adipiscing elit. Donec et turpis vel nulla ultrices malesuada. Pellentesque condimentum mattis tristique. Quisque malesuada ultrices elit, vitae imperdiet enim bibendum sit amet.</p>

  <div class="abs service-item" style="left:538px;top:500px">
    <svg width="34" height="52" viewBox="0 0 34 52" fill="none" stroke="#fff" stroke-width="1.6"><circle cx="20" cy="10" r="8"/><path d="M6 18v14h14v8M14 40v10M6 26h12"/></svg>GUTTERS</div>
  <div class="abs service-item" style="left:834px;top:502px">
    <svg width="44" height="44" viewBox="0 0 44 44" fill="none" stroke="#fff" stroke-width="1.8"><rect x="2" y="2" width="40" height="38"/><rect x="7" y="7" width="30" height="28"/><path d="M22 7v28M7 20h30M0 42h44"/></svg>WINDOWS</div>
  <div class="abs service-item" style="left:534px;top:608px">
    <svg width="38" height="28" viewBox="0 0 38 28" fill="none" stroke="#fff" stroke-width="1.6"><path d="M3 4v22M11 4v22M19 4v22M27 4v22M35 4v22M1 10h36M1 20h36"/></svg>FENCING</div>
  <div class="abs service-item" style="left:840px;top:602px">
    <svg width="40" height="38" viewBox="0 0 40 38" fill="none" stroke="#fff" stroke-width="1.6"><rect x="14" y="2" width="22" height="10" rx="2" transform="rotate(30 25 7)"/><path d="M16 14l-8 10 4 4M10 26l-6 10"/></svg>PAINTING</div>
</section>

<section class="abs endorse">
  <div class="abs endorse-photo" role="img" aria-label="Modern building facade with grey cladding and tall windows"></div>
  <svg class="abs" style="left:200px;top:558px" width="690" height="140" viewBox="0 0 690 140">
    <path d="M677 0v90c0 22-14 36-36 36H250" fill="none" stroke="#000" stroke-width="9"/>
    <path d="M460 126H230" stroke="#e10b0b" stroke-width="9"/>
    <path d="M220 126H20" stroke="#e10b0b" stroke-width="9" stroke-dasharray="40 20"/>
    <path d="M14 100c0 16 8 26 22 26" fill="none" stroke="#e10b0b" stroke-width="9"/>
  </svg>
  <div class="abs endorse-card">
    <h2 class="abs display section-title">Neighbour recognize and<br><span class="accent" style="color:var(--red)">endourse us</span></h2>
    <p class="abs endorse-points">knowledgeable in the insurance claim process<br>fair pricing and quality materials</p>
  </div>
</section>

<section class="abs partners" aria-label="Material partners">
  <div class="partner" style="left:36px"><span class="dot"></span><span>Harrowgate<small>Roofing Products</small></span></div>
  <div class="partner" style="left:236px"><span>Stoneleaf<small>Roofing Group</small></span></div>
  <div class="partner" style="left:428px"><span class="dot"></span><span>Harrowgate<small>Roofing Products</small></span></div>
  <div class="partner" style="left:628px"><span>Stoneleaf<small>Roofing Group</small></span></div>
  <div class="partner" style="left:829px"><span class="dot"></span><span>Harrowgate<small>Roofing Products</small></span></div>
  <div class="partner" style="left:1029px"><span>Stoneleaf<small>Roofing Group</small></span></div>
</section>

<section class="abs process">
  <h2 class="abs display process-title">A simple and &nbsp;<span class="shade">Streamlined<br>Process</span></h2>
  <p class="abs process-tagline">Better Experience /<br>Brambletop Shingle</p>
  <div class="step" style="left:50px" role="img" aria-label="Step one photo"><span class="num">01</span></div>
  <div class="step" style="left:427px" role="img" aria-label="Step two photo"><span class="num">02</span></div>
  <div class="step" style="left:806px" role="img" aria-label="Step three photo"><span class="num">03</span></div>
</section>

</body>
</html>
```